Product and Services Brochure for an Oil and Gas Business

Need a brochure design for our Products and Services. I've attached expectations, Product Names, Picture link, Logo. Please ask if you have any questions.

Use Black and/or White background and related bright colors per our logo colors. Design will have black silk laminate and SPOT UV. Hence please define the respective layers and incorporate those feature in the design. Be bold, modern and unique. No cluttered designs.

Pictures link https://files.brindlevault.net/share/7QkT2mWz9pLx4RcVn8JdYe3HsGa6bUo?view=open

Logos - There are two logos that we use. One for square spaces and one for horizontal spaces

Target Market(s)

Industrial

Colors

Designer to choose colors to be used in the design.

Requirements
Must have
• Clean, uncluttered and bold design with good color pairing
Nice to have
• Pictures provided have both black and transparent backgrounds. It will be great (not sure how) but keep the background dynamic so no product pic gets lost or have weird lines
Should not have
• Too much color

```html
<!DOCTYPE html>
<html lang="en">
<head>
<meta charset="utf-8">
<title>NOVARA and Linden Pro Brochure</title>
<link href="https://fonts.googleapis.com/css2?family=Exo+2:wght@600;700&family=Questrial&display=swap" rel="stylesheet">
<style>
  :root {
    --page-bg: #f1f1f1;
    --sheet: #ffffff;
    --ink: #111111;
    --red: #b5121b;
    --band-black: #0b0b0b;
    --band-grey: #5a5a5a;
    --light-text: #f2f2f2;
  }
  html, body {
    margin: 0;
    padding: 0;
    width: 1200px;
    height: 757px;
    overflow: hidden;
    background: var(--page-bg);
  }
  .sheet {
    position: absolute;
    left: 65px;
    top: 0;
    width: 1070px;
    height: 757px;
    background: var(--sheet);
    overflow: hidden;
  }
  .band { position: absolute; }
  .band--novara {
    left: 661px;
    top: 51px;
    width: 409px;
    height: 166px;
    background: linear-gradient(90deg, var(--band-black) 0%, #1b1b1b 45%, var(--band-grey) 100%);
  }
  .band--linden {
    left: 0;
    top: 537px;
    width: 751px;
    height: 194px;
    background: linear-gradient(90deg, #3a3a3a 0%, #111 55%, var(--band-black) 100%);
  }
  .photo {
    position: absolute;
    border-radius: 28px;
  }
  .photo--novara {
    left: 197px;
    top: 26px;
    width: 473px;
    height: 265px;
    transform: rotate(-51deg);
    background: linear-gradient(200deg, #7e8b98 0%, #9ea4a8 35%, #8d8a86 60%, #6f6c69 100%);
  }
  .photo--linden {
    left: 691px;
    top: 432px;
    width: 446px;
    height: 277px;
    transform: rotate(-48deg);
    background: linear-gradient(200deg, #a4adb4 0%, #b5b2ad 35%, #8f8b86 65%, #6e6b67 100%);
  }
  .product-title {
    position: absolute;
    margin: 0;
    font-family: "Questrial", sans-serif;
    font-size: 25px;
    font-weight: 400;
    color: var(--red);
    display: flex;
    align-items: flex-end;
    gap: 4px;
    white-space: nowrap;
  }
  .product-title .rule {
    display: block;
    height: 3px;
    background: var(--red);
    margin-bottom: 5px;
  }
  .product-title--novara { right: 52px; top: 75px; }
  .product-title--novara .rule { width: 222px; }
  .product-title--linden { left: 58px; top: 553px; }
  .product-title--linden .rule { width: 500px; }
  .product-copy {
    position: absolute;
    margin: 0;
    font-family: "Questrial", sans-serif;
    font-size: 22px;
    line-height: 31px;
    color: var(--light-text);
  }
  .product-copy--novara { right: 52px; top: 108px; text-align: right; }
  .product-copy--linden { left: 57px; top: 587px; }
  .list-rule {
    position: absolute;
    width: 3px;
    background: var(--red);
  }
  .list-rule--applications { left: 59px; top: 0; height: 535px; }
  .list-rule--features { left: 542px; top: 262px; height: 273px; }
  .list-label {
    position: absolute;
    margin: 0;
    font-family: "Exo 2", sans-serif;
    font-weight: 700;
    font-size: 24px;
    letter-spacing: 1px;
    color: var(--red);
    transform-origin: left top;
    transform: rotate(-90deg);
    white-space: nowrap;
  }
  .list-label--applications { left: 31px; top: 525px; }
  .list-label--features { left: 515px; top: 525px; }
  .point-list {
    position: absolute;
    margin: 0;
    padding: 0;
    list-style: none;
    font-family: "Exo 2", sans-serif;
    font-weight: 600;
    font-size: 22px;
    color: var(--ink);
    white-space: nowrap;
  }
  .point-list li::before { content: "*"; margin-right: 3px; }
  .point-list--applications { left: 67px; top: 290px; line-height: 46px; }
  .point-list--features { left: 549px; top: 296px; line-height: 38px; }
</style>
</head>
<body>
  <main class="sheet">
    <div class="band band--novara"></div>
    <div class="band band--linden"></div>

    <div class="photo photo--novara" role="img" aria-label="Product photo of the NOVARA inspection tool resting on gravel at a pipeline site"></div>
    <div class="photo photo--linden" role="img" aria-label="Product photo of the Linden Pro tool resting on gravel"></div>

    <h2 class="product-title product-title--novara"><span class="rule"></span>NOVARA</h2>
    <p class="product-copy product-copy--novara">A versatile platform<br>all Geometry and Mapping<br>Inspection requirements</p>

    <span class="list-rule list-rule--applications"></span>
    <h3 class="list-label list-label--applications">APPLICATIONS</h3>
    <ul class="point-list point-list--applications">
      <li>Go-NoGo</li>
      <li>Compliance</li>
      <li>New Construction</li>
      <li>Probing</li>
      <li>Pre / Post Hydro</li>
    </ul>

    <span class="list-rule list-rule--features"></span>
    <h3 class="list-label list-label--features">FEATURES:</h3>
    <ul class="point-list point-list--features">
      <li>Upto 35% Collapsiblity</li>
      <li>Back to Back Bends</li>
      <li>Upto 75% lighter</li>
      <li>Direct Wall option</li>
      <li>HD and Deformation</li>
      <li>IMU Mapping</li>
    </ul>

    <h2 class="product-title product-title--linden">Linden Pro<span class="rule"></span></h2>
    <p class="product-copy product-copy--linden">For the price of a Gauge Plate tool,<br>run a Caliper with a Gauge plate.<br>If Gauge Plate looks concerning,<br>ask for the geometry report</p>
  </main>
</body>
</html>
```